2 Elite Law Firms on 1 double-sided monument Sign

The original story: 2 separate law firms already have their own perfect individual sign monuments, one for each firm. However, we must now combine them into 1 monument.

Target Market(s)

high-end clientele

Industry/Entity Type

Legal

Requirements
Must have
• Sleek, equal representation of both firms.

```html
<!DOCTYPE html>
<html lang="en">
<head>
<meta charset="utf-8">
<title>Shared Monument Sign – Harlow &amp; Partners / Kessler Law Group</title>
<link rel="stylesheet" href="https://fonts.googleapis.com/css2?family=Cinzel:wght@400;600&display=swap">
<style>
  :root {
    --canvas: #f0f0f0;
    --brown-top: #673e25;
    --brown-bottom: #391c11;
    --brown-base: #47251a;
    --navy-top: #253479;
    --navy-bottom: #131a52;
    --navy-base: #1b2462;
    --ink: #ffffff;
    --number-ink: #f2f2f2;
  }
  * { margin: 0; padding: 0; box-sizing: border-box; }
  html, body {
    width: 1200px;
    height: 2400px;
    overflow: hidden;
    background: var(--canvas);
  }
  .canvas {
    position: relative;
    width: 1200px;
    height: 2400px;
    font-family: "Cinzel", "Times New Roman", serif;
    color: var(--ink);
  }
  .monument {
    position: absolute;
    left: 116px;
    width: 968px;
  }
  .monument--north { top: 373px; }
  .monument--south { top: 1420px; }

  .sign-face {
    display: flex;
    height: 504px;
  }
  .firm-panel {
    position: relative;
    flex: 1 1 50%;
    display: flex;
    flex-direction: column;
    align-items: center;
  }
  .firm-panel--harlow {
    background: linear-gradient(180deg, var(--brown-top) 0%, var(--brown-bottom) 100%);
  }
  .firm-panel--kessler {
    background: linear-gradient(180deg, var(--navy-top) 0%, var(--navy-bottom) 100%);
  }

  .firm-name {
    position: absolute;
    top: 148px;
    left: 0;
    right: 0;
    height: 150px;
    display: flex;
    flex-direction: column;
    align-items: center;
    justify-content: center;
    font-weight: 400;
    text-align: center;
    line-height: 1;
  }
  .firm-name__main {
    font-size: 54px;
    letter-spacing: 3px;
  }
  .firm-name__second {
    font-size: 44px;
    letter-spacing: 2px;
    margin-top: 8px;
  }
  .firm-name__tagline {
    font-size: 22px;
    letter-spacing: 2px;
    margin-top: 12px;
  }
  .firm-name__row {
    display: flex;
    align-items: center;
    gap: 18px;
  }
  .firm-name__square {
    width: 30px;
    height: 30px;
    background: var(--ink);
  }
  .firm-name__spaced {
    font-size: 22px;
    letter-spacing: 9px;
    margin-top: 14px;
  }

  .street-number {
    position: absolute;
    top: 392px;
    left: 0;
    right: 0;
    text-align: center;
    font-size: 62px;
    font-weight: 400;
    color: var(--number-ink);
    letter-spacing: 1px;
    line-height: 1;
  }

  .plinth {
    display: flex;
    width: 782px;
    height: 84px;
    margin-left: 93px;
  }
  .plinth__half { flex: 1 1 50%; }
  .plinth__half--harlow { background: var(--brown-base); }
  .plinth__half--kessler { background: var(--navy-base); }
</style>
</head>
<body>
<main class="canvas">

  <section class="monument monument--north" aria-label="Monument sign, street-facing side">
    <div class="sign-face">
      <div class="firm-panel firm-panel--harlow">
        <div class="firm-name">
          <span class="firm-name__main">HARLOW</span>
          <span class="firm-name__second">&amp; PARTNERS</span>
          <span class="firm-name__tagline">ATTORNEYS AT LAW</span>
        </div>
        <p class="street-number">412</p>
      </div>
      <div class="firm-panel firm-panel--kessler">
        <div class="firm-name">
          <div class="firm-name__row">
            <span class="firm-name__square"></span>
            <span class="firm-name__main">KESSLER</span>
          </div>
          <span class="firm-name__spaced">LAW GROUP</span>
        </div>
        <p class="street-number">410</p>
      </div>
    </div>
    <div class="plinth">
      <div class="plinth__half plinth__half--harlow"></div>
      <div class="plinth__half plinth__half--kessler"></div>
    </div>
  </section>

  <section class="monument monument--south" aria-label="Monument sign, reverse side">
    <div class="sign-face">
      <div class="firm-panel firm-panel--kessler">
        <div class="firm-name">
          <div class="firm-name__row">
            <span class="firm-name__square"></span>
            <span class="firm-name__main">KESSLER</span>
          </div>
          <span class="firm-name__spaced">LAW GROUP</span>
        </div>
        <p class="street-number">410</p>
      </div>
      <div class="firm-panel firm-panel--harlow">
        <div class="firm-name">
          <span class="firm-name__main">HARLOW</span>
          <span class="firm-name__second">&amp; PARTNERS</span>
          <span class="firm-name__tagline">ATTORNEYS AT LAW</span>
        </div>
        <p class="street-number">412</p>
      </div>
    </div>
    <div class="plinth">
      <div class="plinth__half plinth__half--kessler"></div>
      <div class="plinth__half plinth__half--harlow"></div>
    </div>
  </section>

</main>
</body>
</html>
```